Massage Clinic needs a Flyer for Advertising

Our massage clinic, 'Keel Street Remedial Therapy', has recently opened in Osborne Park, Western Australia. We are specialists in deep tissue and sports massage. We also offer relaxation, trigger point therapy, stretching techniques, and postural and functional movement analysis. We're based within the same building complex as a personal training and IronForge box. There are also a number of local gyms in the area. Our target clients are both the local athletes, but also local business (Osborne Park is a business district in Perth).

We need double-sided DL size flyer. We would like the design to incorporate the colouring of the logo (green, purple, grey), but happy for it to use anything that enhances this also. Logo has been attached (.png and .ai format). There is also a selection of photos available to use if required, other stylised images would also be accepted. We'd like the flyer to include business details, services, and price list (price list is optional). We can provide further descriptions of key therapies on offer if required for inclusion.

Target Market(s)

Local athletes (gym, IronForge, sport), and local business employees.

Industry/Entity Type

Massage Therapy

Font styles to use
Sans Serif

Requirements
Must have
• List of Services to be included:
• Relaxation Massage
• Deep Tissue Massage
• Sports Massage
• Neuromuscular (Trigger Point) Therapy
• Postural Analysis
• Musculoskeletal and Functional Movement Screening
• Therapeutic Stretching (including Proprioceptive Neuromuscular Facilitation and Muscle Energy Technique)
• All sessions are customised to suit the needs of the client, and may incorporate a variety of the above techniques.
• Business location and Contact details:
• 4/61 Tarrant Lane, Osborne Park WA 6017
• Phone: 0412 573 604
• Email: info@keelstreet.example.net
Nice to have
• Symbols for showing the company has Chatterly and Snapframe accounts.
• The business is also a member of NRTG - logo attached below, please include.
• Price details are shown in one of the attached images, and copied below:
• Individual -
• 30 minutes $45
• 60 minutes $85
• Packages -
• 4 x 30 minutes $165
• 4 x 60 minutes $305
• (Packages valid for two months; pre-payment required).
Should not have
• Please don't use any imagery/design that looks suited to a day-spa environment. My massage clinic is located within a gym environment.
• If you use stock photo's, please select one where the therapists hands are female (both are stuff are currently female therapists).

```html
<!DOCTYPE html>
<html lang="en">
<head>
<meta charset="utf-8">
<title>Keel Street Remedial Therapy – DL Flyer</title>
<link rel="stylesheet" href="https://fonts.googleapis.com/css2?family=Arimo:ital,wght@0,400;0,700;1,400;1,700&family=Mulish:ital,wght@0,500;0,700;1,500&display=swap">
<style>
  :root {
    --ink: #000000;
    --paper: #ffffff;
    --purple: #6a2e92;
    --green: #7dbb3c;
    --grey: #5a5a5a;
    --text: #1e1e1e;
    --towel-dark: #3c3532;
    --towel-mid: #6e6561;
  }
  * { box-sizing: border-box; margin: 0; padding: 0; }
  html, body { width: 1200px; height: 1000px; overflow: hidden; background: var(--ink); }
  .sheet { position: relative; width: 1200px; height: 1000px; background: var(--ink); font-family: "Arimo", sans-serif; }

  .side-label {
    position: absolute; width: 200px; text-align: center;
    color: var(--paper); font-family: "Arimo", sans-serif; font-weight: 700;
    font-size: 28px; letter-spacing: 1px;
  }
  .side-label--left { left: -62px; transform: rotate(-90deg); }
  .side-label--right { left: 1062px; transform: rotate(90deg); }
  .side-label--front { top: 232px; }
  .side-label--back { top: 732px; }

  /* Front */
  .front { position: absolute; left: 76px; top: 0; width: 1048px; height: 497px; overflow: hidden; }
  .front__photo {
    position: absolute; inset: 0;
    background: linear-gradient(200deg, var(--paper) 0%, var(--paper) 30%, #b9b1ad 42%, var(--towel-mid) 55%, var(--towel-dark) 100%);
  }
  .brand { position: absolute; display: flex; align-items: center; gap: 14px; color: var(--purple); font-family: "Mulish", sans-serif; font-weight: 500; }
  .brand__dot { border-radius: 50%; background: var(--green); flex: none; }
  .brand__name { line-height: 1.05; }
  .brand__line { display: block; }
  .front .brand { right: 40px; top: 62px; }
  .front .brand__dot { width: 54px; height: 54px; }
  .front .brand__line--main { font-size: 56px; }
  .front .brand__line--sub { font-size: 32px; }

  .front__contact {
    position: absolute; left: 0; top: 453px; width: 100%; height: 24px;
    color: var(--paper); font-family: "Arimo", sans-serif; font-weight: 700; font-size: 17px;
  }
  .front__contact span { position: absolute; top: 0; }
  .contact-address { left: 30px; }
  .contact-email { left: 580px; }
  .contact-phone { left: 894px; }

  /* Back */
  .back { position: absolute; left: 76px; top: 500px; width: 1048px; height: 500px; background: var(--green); padding: 17px 16px 15px; }
  .back__panel { position: relative; width: 100%; height: 100%; background: var(--paper); }
  .back .brand { left: 48px; top: 46px; }
  .back .brand__dot { width: 34px; height: 34px; }
  .back .brand__line--main { font-size: 36px; }
  .back .brand__line--sub { font-size: 21px; color: var(--purple); }

  .prices { position: absolute; left: 34px; top: 157px; width: 420px; color: var(--text); }
  .prices__heading { font-weight: 700; font-style: italic; font-size: 19px; margin-bottom: 2px; }
  .prices__group + .prices__group { margin-top: 26px; }
  .price-row { display: flex; align-items: baseline; font-size: 19px; line-height: 25px; padding-left: 8px; }
  .price-row__leader { flex: 1; border-bottom: 1px solid var(--text); margin: 0 4px; transform: translateY(-3px); }
  .price-row__amount { width: 42px; }
  .prices__note { font-style: italic; font-size: 13px; padding-left: 8px; }
  .prices__mobile { position: absolute; left: 34px; top: 384px; font-size: 18px; color: var(--text); }

  .membership { position: absolute; left: 498px; top: 358px; display: flex; align-items: center; gap: 8px; }
  .membership__badge { width: 30px; height: 34px; background: #1f4fa0; border-radius: 4px; }
  .membership__name { font-size: 10.5px; line-height: 11px; color: var(--text); text-transform: uppercase; width: 130px; }

  .services { position: absolute; right: 38px; top: 27px; text-align: right; list-style: none; color: var(--purple); font-family: "Mulish", sans-serif; }
  .services li { font-weight: 700; font-size: 19.5px; line-height: 25px; margin-bottom: 18px; }
  .services li.two-line { margin-bottom: 19px; }
  .services__detail { display: block; font-weight: 500; font-style: italic; line-height: 25px; }

  .back__footnote { position: absolute; left: 34px; top: 430px; font-style: italic; font-size: 16px; color: var(--text); }
</style>
</head>
<body>
<main class="sheet">
  <span class="side-label side-label--left side-label--front">FRONT</span>
  <span class="side-label side-label--right side-label--front">FRONT</span>
  <span class="side-label side-label--left side-label--back">BACK</span>
  <span class="side-label side-label--right side-label--back">BACK</span>

  <section class="front">
    <div class="front__photo" role="img" aria-label="Photograph of rolled charcoal towels on a massage table with a red lily flower"></div>
    <div class="brand">
      <span class="brand__dot"></span>
      <span class="brand__name">
        <span class="brand__line brand__line--main">Keel Street</span>
        <span class="brand__line brand__line--sub">Remedial Therapy</span>
      </span>
    </div>
    <div class="front__contact">
      <span class="contact-address">4/61 Tarrant Lane, Osborne Park, WA&nbsp;&nbsp;6017</span>
      <span class="contact-email">info@keelstreet.example.net</span>
      <span class="contact-phone">0412 573 604</span>
    </div>
  </section>

  <section class="back">
    <div class="back__panel">
      <div class="brand">
        <span class="brand__dot"></span>
        <span class="brand__name">
          <span class="brand__line brand__line--main">Keel Street</span>
          <span class="brand__line brand__line--sub">Remedial Therapy</span>
        </span>
      </div>

      <div class="prices">
        <div class="prices__group">
          <p class="prices__heading">Individual Sessions:</p>
          <p class="price-row"><span>30 minutes</span><span class="price-row__leader"></span><span class="price-row__amount">$45</span></p>
          <p class="price-row"><span>60 minutes</span><span class="price-row__leader"></span><span class="price-row__amount">$85</span></p>
        </div>
        <div class="prices__group">
          <p class="prices__heading">Packages:</p>
          <p class="price-row"><span>4 x 30 minutes</span><span class="price-row__leader"></span><span class="price-row__amount">$165</span></p>
          <p class="price-row"><span>4 x 60 minutes</span><span class="price-row__leader"></span><span class="price-row__amount">$305</span></p>
          <p class="prices__note">(Packages valid for two months. Pre-payment required.)</p>
        </div>
      </div>
      <p class="prices__mobile">Price for mobile appointments on request.</p>

      <div class="membership">
        <span class="membership__badge"></span>
        <span class="membership__name">National Remedial Therapists Guild</span>
      </div>

      <ul class="services">
        <li>Relaxation Massage</li>
        <li>Deep Tissue Massage</li>
        <li>Sports Massage</li>
        <li>Neuromuscular (Trigger Point) Therapy</li>
        <li>Postural Analysis</li>
        <li class="two-line">Musculoskeletal &amp;<br>Functional Movement Screening</li>
        <li>Therapeutic Stretching
          <span class="services__detail">(including Proprioceptive<br>Neuromuscular Facilitation<br>&amp; Muscle Energy Technique)</span>
        </li>
      </ul>

      <p class="back__footnote">All sessions are customised to suit the needs of the client, &amp; may incorporate a variety of the above techniques.</p>
    </div>
  </section>
</main>
</body>
</html>
```